Lantern Above the Harbor ~ An Unbinding Passage for Versemakers

My book is called “Lantern Above the Harbor.” Its subtitle is “An Unbinding Passage for Versemakers.” It is a book about being a poet, writing poetry, and the ways in which poets are connected to both society and the central energy of the Universe. I want the cover design to be abstract and impressionistic. A suggestion of fireworks or a starburst would be a plus. To be consistent with the 3 other books I have published, I want the font for the title, as well as my name (Dorothea Halvik) to be Papyrus. The subtitle font can be something more plain and sans serif, like Arial or Franklin Gothic Book, probably in italics. As for color, I definitely want pale gold (angelic). Possible other complimentary colors could be either light or dark shades of gray, turquoise, rose, rust or red. I'm attaching the back cover text and also three pages from inside the book that have line drawings, to give an example of the interior artwork.
Updates

Forgot to mention: My book is a paperback. Its size will be 8.5" high and 5.5" wide. I'm self-publishing it, and it will be printed by Quillby Press in Nebraska, USA. It has 104 pages. I think you need the number of pages, in order to make the spine of the book the correct width.

Target Market(s)

My target market is people who write poetry or are interested in how poetry is written.

Industry/Entity Type

Poetry

Font styles to use
Sans Serif
Other font styles liked:
• Papyrus for the front cover. Arial or another sans serif font on the back cover.

Colors

Designer to choose colors to be used in the design.

Requirements
Must have
• My book cover needs to be inspiring and uplifting, as well as abstract and impressionistic, with kind of a "New Age" feel. I don't want anything that looks rigid and scholarly.
Nice to have
• The book talks about the connection poets have to the Universe and the Creative Energy at the center of everything. The cover should convey that Energy.
Should not have
• My cover should not be realistic, logical or straight-laced. I want something that feels free, imaginative and unfettered.

```html
<!DOCTYPE html>
<html lang="en">
<head>
<meta charset="utf-8">
<title>Lantern Above the Harbor – cover spread</title>
<link rel="stylesheet" href="https://fonts.googleapis.com/css2?family=Macondo&family=Open+Sans:ital,wght@0,400;0,700;1,400;1,700&display=swap">
<style>
  :root {
    --paper: #ffffff;
    --cover-orange: #f8a13a;
    --cover-deep: #f08a1c;
    --cover-light: #fcd28a;
    --ink: #1c1a17;
    --trim: #b9b9b9;
    --photo-tone: #b7a596;
    --ornament-tone: #c9762a;
  }
  * { box-sizing: border-box; margin: 0; padding: 0; }
  html, body { width: 1200px; height: 942px; overflow: hidden; background: var(--paper); }
  .sheet { position: relative; width: 1200px; height: 942px; background: var(--paper); font-family: "Open Sans", Arial, sans-serif; color: var(--ink); }

  .trim-marks { position: absolute; inset: 0; }

  .cover { position: absolute; left: 72px; top: 69px; width: 1056px; height: 802px; background: var(--cover-orange); overflow: hidden; }

  .front-art {
    position: absolute; left: 541px; top: 0; width: 515px; height: 802px;
    background:
      radial-gradient(ellipse 180px 120px at 62% 30%, rgba(255,236,190,.55), transparent 70%),
      radial-gradient(ellipse 240px 90px at 40% 52%, rgba(255,225,160,.45), transparent 70%),
      radial-gradient(circle 70px at -9% 71%, rgba(255,245,215,.8), transparent 70%),
      linear-gradient(160deg, var(--cover-light) 0%, var(--cover-orange) 40%, var(--cover-deep) 100%);
  }
  .flare { position: absolute; left: 480px; top: 530px; width: 120px; height: 120px; border-radius: 50%;
    background: radial-gradient(circle, rgba(255,248,225,.9) 0%, rgba(255,230,170,.35) 35%, transparent 70%); }

  .back { position: absolute; left: 35px; top: 0; width: 446px; font-size: 13.6px; line-height: 1.32; }
  .back p { text-align: justify; margin-bottom: 9px; }
  .back em.book { font-weight: 700; font-style: italic; }
  .back .lead-in { position: absolute; top: 27px; }
  .back .chapters-intro { position: absolute; top: 201px; width: 446px; text-align: center; }
  .back .chapters { position: absolute; top: 232px; width: 446px; text-align: center; font-size: 13px; line-height: 1.7; letter-spacing: .2px; }
  .back .ornament { position: absolute; left: 154px; top: 296px; width: 117px; height: 46px; background: var(--ornament-tone); border-radius: 60% 40% 55% 45% / 70% 60% 40% 30%; opacity: .85; }
  .back .author-photo { position: absolute; left: 0; top: 357px; width: 128px; height: 143px; background: linear-gradient(160deg, #d9cfc6, var(--photo-tone)); }
  .back .bio { position: absolute; left: 138px; top: 355px; width: 308px; }
  .back .praise { position: absolute; top: 550px; }
  .barcode-box { position: absolute; left: 293px; top: 648px; width: 188px; height: 118px; background: var(--paper); }

  .spine { position: absolute; left: 513px; top: 0; width: 28px; height: 802px; }
  .spine-text { position: absolute; left: 6px; writing-mode: vertical-rl; font-size: 11.5px; letter-spacing: 2.6px; text-transform: uppercase; color: var(--ink); }
  .spine-title { top: 36px; }
  .spine-author { top: 562px; }

  .front-title { position: absolute; left: 541px; top: 140px; width: 515px; text-align: center; font-family: "Macondo", "Papyrus", fantasy; color: var(--ink); line-height: .95; }
  .front-title .line-1 { display: block; font-size: 78px; padding-left: 100px; }
  .front-title .line-2 { display: block; font-size: 58px; padding-left: 110px; }
  .front-title .line-3 { display: block; font-size: 74px; padding-left: 60px; }
  .subtitle { position: absolute; left: 541px; top: 390px; width: 515px; text-align: center; padding-left: 50px; font-size: 19px; color: var(--ink); }
  .front-author { position: absolute; left: 541px; top: 722px; width: 515px; text-align: center; padding-left: 30px; font-family: "Macondo", "Papyrus", fantasy; font-size: 40px; color: var(--ink); }

  .spec { position: absolute; top: 893px; font-weight: 700; font-size: 17px; }
  .spec-size { left: 230px; }
  .spec-version { left: 392px; }
</style>
</head>
<body>
<div class="sheet">
  <svg class="trim-marks" width="1200" height="942" aria-hidden="true">
    <g stroke="var(--trim)" stroke-width="1">
      <line x1="72" y1="0" x2="72" y2="48"/><line x1="1128" y1="0" x2="1128" y2="48"/>
      <line x1="0" y1="69" x2="52" y2="69"/><line x1="1148" y1="69" x2="1200" y2="69"/>
      <line x1="72" y1="892" x2="72" y2="942"/><line x1="1128" y1="892" x2="1128" y2="942"/>
      <line x1="0" y1="871" x2="52" y2="871"/><line x1="1148" y1="871" x2="1200" y2="871"/>
      <g stroke-dasharray="4 3">
        <line x1="585" y1="0" x2="585" y2="60"/><line x1="613" y1="0" x2="613" y2="60"/>
        <line x1="585" y1="880" x2="585" y2="942"/><line x1="613" y1="880" x2="613" y2="942"/>
      </g>
    </g>
  </svg>

  <div class="cover">
    <div class="front-art" role="img" aria-label="Abstract swirling orange and gold firework light streams"></div>
    <div class="flare" role="img" aria-label="Soft lens flare glow"></div>

    <section class="back">
      <p class="lead-in" style="width:446px"><em class="book">Lantern Above the Harbor</em> is indeed “An Unbinding Passage for Versemakers.” It is written by Dorothea Halvik, an exciting, imaginative voice in American poetry.</p>
      <p style="position:absolute;top:84px;width:446px">In <em class="book">Lantern Above the Harbor</em>, Dorothea discusses the essential elements of poetry and the process of writing it. She offers an inspiring view of the mission of poets and their connection to both society and the larger forces in the Universe. Her book is motivational, refreshing and irrepressibly optimistic.</p>
      <p class="chapters-intro">The seven intriguing chapters in <em class="book">Lantern Above the Harbor</em> are</p>
      <p class="chapters">LIBERATION ~ EXPERIENCE ~ WORDS ~ POETRY ~<br>INTEGRITY ~ BEAUTY ~ CREATION</p>
      <div class="ornament" role="img" aria-label="Small line-drawn leaf ornament"></div>
      <div class="author-photo" role="img" aria-label="Portrait photo of the author"></div>
      <p class="bio">For over 50 years, Dorothea has been a teacher of writing and poetry. Since 2007, she has published three books of her poems: <em>Tending the Rain Barrel</em>, <em>The Velvet Hem of Someday</em> and <em>The Wide Linen Hush</em>. Her work overflows with her characteristically rich images and quirky metaphors. It runs the gamut from subtle eroticism to abject grief, from defiant rage to philosophical meditation, and from borderline blasphemy to lyrical fantasy.</p>
      <p class="praise" style="width:446px">Dorothea has been called by critic Gideon Rafferty “a poet to be reckoned with; bright, feisty, compassionate.” (<em>The Morning Ledger</em>, Ashford, OH). Author Celia Marwood (“<em>Larkspur Row</em>,” 2011) says Dorothea’s poetry is like “a perpetual Surprise Party ~ memorable, insightful and thematically fascinating.”</p>
    </section>
    <div class="barcode-box"></div>

    <div class="spine">
      <span class="spine-text spine-title">Lantern Above the Harbor</span>
      <span class="spine-text spine-author">Dorothea Halvik</span>
    </div>

    <h1 class="front-title">
      <span class="line-1">Lantern</span>
      <span class="line-2">Above the</span>
      <span class="line-3">Harbor</span>
    </h1>
    <p class="subtitle">An Unbinding Passage for Versemakers</p>
    <p class="front-author">Dorothea Halvik</p>
  </div>

  <span class="spec spec-size">5.5 x 8.5</span>
  <span class="spec spec-version">V1.0</span>
</div>
</body>
</html>
```